CASH PAYMENT DISCOUNT NOTICE POSTED IN CASH REGISTER AREA

LOOKING TO MAKE A FLYER OR A POSTED NOTICE FOR CUSTOMERS PAYING FOR OVER-THE-COUNTER MERCHANDISE AND WHO PAY BY CASH METHOD TO GET A 4% CASH DISCOUNT.
PRESCRIPTIONS ARE EXCLUDED FROM THIS CASH DISCOUNT.

Target Market(s)

RETAIL CUSTOMERS

Industry/Entity Type

RETAIL PHARMACY

Colors
0054AA
0677BA
7BADD7
CADEEF
E8F1F8
EB3D1F
EC4F4E
F09395
F8D3D4
FCEDEE

Requirements
Must have
• LOGO COLORS
Nice to have
• EYE CATCHING

```html
<!DOCTYPE html>
<html lang="en">
<head>
<meta charset="utf-8">
<title>Hale Street Pharmacy – 4% Cash Discount Notice</title>
<link rel="stylesheet" href="https://fonts.googleapis.com/css2?family=Anton&family=Poppins:ital,wght@0,600;0,700;0,800;1,700&display=swap">
<style>
  :root {
    --stage: #e9ebee;
    --blue-top: #0a8cff;
    --blue-mid: #0569d6;
    --blue-deep: #00349a;
    --blue-brand: #0054AA;
    --blue-soft: #7BADD7;
    --blue-pale: #CADEEF;
    --red-deep: #b01f24;
    --red-bright: #EB3D1F;
    --orange: #f05a22;
    --white: #ffffff;
    --social: #3aa8f0;
  }
  * { box-sizing: border-box; margin: 0; padding: 0; }
  html, body { width: 1200px; height: 1200px; overflow: hidden; }
  body { background: var(--stage); position: relative; font-family: "Poppins", sans-serif; }

  .notice {
    position: absolute; left: 150px; top: 17px;
    width: 900px; height: 1166px; overflow: hidden;
    background: linear-gradient(180deg, var(--blue-top) 0%, var(--blue-mid) 45%, var(--blue-deep) 100%);
    box-shadow: 0 18px 30px rgba(0, 30, 80, .25);
  }
  .notice__glow {
    position: absolute; inset: 0;
    background: radial-gradient(ellipse 420px 320px at 450px 170px, rgba(160, 210, 255, .65), rgba(160, 210, 255, 0) 70%);
  }
  .notice__rays { position: absolute; inset: 0; }

  .brand-tab { position: absolute; left: 0; top: 0; width: 900px; height: 140px; }
  .brand {
    position: absolute; left: 0; top: 38px; width: 900px;
    display: flex; align-items: center; justify-content: center; gap: 12px;
  }
  .brand__dot { width: 22px; height: 22px; border-radius: 50%; background: var(--red-deep); }
  .brand__name { font-weight: 700; font-size: 30px; color: var(--red-deep); letter-spacing: .5px; }

  .headline-box {
    position: absolute; left: 96px; top: 191px; width: 708px; height: 83px;
    border: 3px solid var(--white); border-radius: 10px;
    box-shadow: 0 3px 8px rgba(0, 40, 110, .35);
    display: flex; align-items: center; justify-content: center;
  }
  .headline-box__text {
    color: var(--white); font-weight: 700; font-size: 53px; letter-spacing: 1px;
    text-shadow: 0 3px 5px rgba(0, 30, 90, .45);
  }

  .offer { position: absolute; left: 0; top: 0; width: 900px; height: 1166px; }
  .offer text { paint-order: stroke fill; stroke-linejoin: round; }
  .offer__percent { font-family: "Poppins", sans-serif; font-weight: 800; }
  .offer__word { font-family: "Anton", sans-serif; }

  .disclaimer {
    position: absolute; left: 0; top: 952px; width: 900px; text-align: center;
    color: var(--white); font-weight: 700; font-style: italic; font-size: 22px;
    text-shadow: 0 2px 4px rgba(0, 30, 90, .5);
  }
  .disclaimer__rule {
    position: absolute; left: 110px; top: 986px; width: 680px; height: 1px;
    background: linear-gradient(90deg, rgba(202,222,239,0), var(--blue-pale), rgba(202,222,239,0));
  }

  .website {
    position: absolute; left: 0; top: 1054px; width: 900px; text-align: center;
    color: var(--white); font-weight: 600; font-size: 24px; letter-spacing: 2px;
  }
  .socials {
    position: absolute; left: 0; top: 1112px; width: 900px;
    display: flex; justify-content: center; gap: 40px;
  }
  .socials__item { display: flex; align-items: center; gap: 14px; }
  .socials__mark { width: 24px; height: 24px; border-radius: 4px; background: var(--social); }
  .socials__handle { color: var(--white); font-weight: 600; font-size: 11.5px; letter-spacing: 1.6px; }
</style>
</head>
<body>
  <main class="notice">
    <div class="notice__glow"></div>

    <svg class="notice__rays" width="900" height="1166" viewBox="0 0 900 1166" aria-hidden="true">
      <g fill="#ffffff" opacity=".12">
        <polygon points="450,300 40,0 70,0"/>
        <polygon points="450,300 200,0 225,0"/>
        <polygon points="450,300 380,0 400,0"/>
        <polygon points="450,300 500,0 518,0"/>
        <polygon points="450,300 690,0 715,0"/>
        <polygon points="450,300 860,0 900,0"/>
        <polygon points="450,300 0,160 0,190"/>
        <polygon points="450,300 0,340 0,365"/>
        <polygon points="450,300 0,490 0,510"/>
        <polygon points="450,300 0,620 0,640"/>
        <polygon points="450,300 0,740 0,760"/>
        <polygon points="450,300 900,110 900,150"/>
        <polygon points="450,300 900,300 900,325"/>
        <polygon points="450,300 900,460 900,480"/>
        <polygon points="450,300 900,600 900,615"/>
        <polygon points="450,300 900,780 900,800"/>
        <polygon points="450,300 0,1020 0,1060"/>
        <polygon points="450,300 30,1166 70,1166"/>
        <polygon points="450,300 270,1166 295,1166"/>
        <polygon points="450,300 460,1166 480,1166"/>
        <polygon points="450,300 640,1166 665,1166"/>
        <polygon points="450,300 870,1166 900,1166"/>
        <polygon points="450,300 900,980 900,1020"/>
      </g>
    </svg>

    <svg class="brand-tab" width="900" height="140" viewBox="0 0 900 140" aria-hidden="true">
      <defs>
        <filter id="tab-shadow" x="-10%" y="-20%" width="120%" height="160%">
          <feDropShadow dx="0" dy="4" stdDeviation="6" flood-color="#00306f" flood-opacity=".35"/>
        </filter>
      </defs>
      <path d="M204 0 H697 L640 112 Q628 134 600 134 H300 Q272 134 260 112 Z" fill="#ffffff" filter="url(#tab-shadow)"/>
    </svg>
    <div class="brand">
      <span class="brand__dot"></span>
      <span class="brand__name">Hale Street Pharmacy</span>
    </div>

    <div class="headline-box"><span class="headline-box__text">PAY CASH AND RECEIVE</span></div>

    <svg class="offer" width="900" height="1166" viewBox="0 0 900 1166" role="img" aria-label="4% cash discount">
      <defs>
        <linearGradient id="percent-fill" x1="0" y1="0" x2="0" y2="1">
          <stop offset="0" stop-color="#b01f24"/>
          <stop offset="1" stop-color="#f05a22"/>
        </linearGradient>
        <linearGradient id="cash-fill" x1="0" y1="0" x2="0" y2="1">
          <stop offset="0" stop-color="#0a7be6"/>
          <stop offset="1" stop-color="#0054AA"/>
        </linearGradient>
        <linearGradient id="discount-fill" x1="0" y1="0" x2="0" y2="1">
          <stop offset="0" stop-color="#0054c0"/>
          <stop offset="1" stop-color="#003590"/>
        </linearGradient>
        <filter id="lift" x="-10%" y="-10%" width="120%" height="130%">
          <feDropShadow dx="0" dy="6" stdDeviation="6" flood-color="#001e5c" flood-opacity=".45"/>
        </filter>
      </defs>

      <text class="offer__percent" x="438" y="551" text-anchor="middle" font-size="272"
            textLength="404" lengthAdjust="spacingAndGlyphs"
            fill="url(#percent-fill)" stroke="#ffffff" stroke-width="16" filter="url(#lift)">4%</text>

      <text class="offer__word" x="444" y="737" text-anchor="middle" font-size="186"
            textLength="355" lengthAdjust="spacingAndGlyphs"
            fill="url(#cash-fill)" stroke="#ffffff" stroke-width="14" filter="url(#lift)">CASH</text>

      <text class="offer__word" x="448" y="916" text-anchor="middle" font-size="222"
            textLength="680" lengthAdjust="spacingAndGlyphs"
            fill="url(#discount-fill)" stroke="#ffffff" stroke-width="14" filter="url(#lift)">DISCOUNT</text>
    </svg>

    <p class="disclaimer">*PRESCRIPTIONS ARE EXCLUDED FROM THIS CASH DISCOUNT*</p>
    <div class="disclaimer__rule"></div>

    <p class="website">www.halestreetrx.com</p>

    <ul class="socials">
      <li class="socials__item"><span class="socials__mark"></span><span class="socials__handle">HALESTREETRX</span></li>
      <li class="socials__item"><span class="socials__mark"></span><span class="socials__handle">HALESTREETRX</span></li>
      <li class="socials__item"><span class="socials__mark"></span><span class="socials__handle">HALESTREETRX</span></li>
    </ul>
  </main>
</body>
</html>
```